Velno Recycling needs a new web design

We need a new web design for our company based in Austin, TX. We resell and recycling electronics such as laptops, computer components, Tovlets, Brunos, etc. Since our inception over ten years ago, we’ve become one of the premier electronics recycling and remarketing companies in Austin, Texas.

```html
<!DOCTYPE html>
<html lang="en">
<head>
<meta charset="utf-8">
<title>Velno Recycling</title>
<link href="https://fonts.googleapis.com/css2?family=Cinzel:wght@600&family=Montserrat:wght@500;600;700&family=Open+Sans:wght@400;600&display=swap" rel="stylesheet">
<style>
:root{
  --blue:#1b74bd;
  --dark:#444546;
  --ink:#222;
  --text:#333;
  --grey-bg:#eeeeee;
  --white:#fff;
}
*{box-sizing:border-box;margin:0;padding:0}
html,body{width:1200px;height:3152px;overflow:hidden;background:var(--white)}
body{font-family:"Open Sans",Arial,sans-serif;color:var(--text);position:relative}
a{color:inherit;text-decoration:none}

.site-header{position:absolute;top:0;left:0;width:1200px;height:120px;background:var(--white);z-index:3}
.brand{position:absolute;left:99px;top:34px;display:flex;align-items:center;gap:12px}
.brand-mark{width:42px;height:42px;border-radius:50%;background:var(--blue)}
.brand-name{font-family:"Montserrat",sans-serif;font-weight:700;font-size:24px;color:var(--blue)}
.contact-pill{position:absolute;top:0;height:42px;border-radius:0 0 12px 12px;color:var(--white);font-size:14.5px;display:flex;align-items:center;justify-content:center;gap:8px;padding:0 14px;white-space:nowrap}
.contact-pill.mail{left:672px;width:263px;background:var(--blue)}
.contact-pill.phone{left:947px;width:154px;background:var(--dark)}
.main-nav{position:absolute;top:72px;right:99px;display:flex;gap:44px;font-family:"Montserrat",sans-serif;font-weight:600;font-size:15px;color:var(--ink)}

.about{position:absolute;top:560px;left:0;width:1200px;height:895px;background:var(--grey-bg);z-index:0}

.hero{position:absolute;top:120px;left:0;width:1200px;height:600px;z-index:1;
  background:linear-gradient(180deg,#4d5456 0%,#3a4540 40%,#2f3b2c 70%,#3d4a33 100%);
  clip-path:polygon(0 0,100% 0,100% 77%,50% 100%,0 77%)}
.hero-body{position:absolute;top:126px;left:0;width:1200px;text-align:center;color:var(--white)}
.hero-title{font-family:"Cinzel",serif;font-weight:600;font-size:62px;letter-spacing:2px}
.hero-lead{width:760px;margin:14px auto 0;font-size:16px;font-weight:600;line-height:1.75}
.btn{display:inline-block;border-radius:30px;font-family:"Montserrat",sans-serif;font-weight:700;text-transform:uppercase;white-space:nowrap}
.hero .btn{margin-top:22px;background:var(--white);color:var(--blue);padding:17px 26px;font-size:14px}
.hero-arrow{position:absolute;top:300px}
.hero-arrow.prev{left:32px}.hero-arrow.next{right:32px}

.features{position:absolute;top:0;left:0;z-index:2}
.feature{position:absolute;background:var(--white);border-radius:170px 170px 80px 80px;overflow:hidden;text-align:center;box-shadow:0 6px 8px rgba(0,0,0,.18)}
.feature.side{width:309px;top:610px;height:482px}
.feature.logistics{left:99px}
.feature.certs{left:793px}
.feature.main{left:420px;top:536px;width:361px;height:577px;border-radius:190px 190px 100px 100px}
.feature-num{margin:0 auto;width:200px;height:142px;border-radius:0 0 100px 100px;background:var(--dark);color:var(--white);font-family:"Montserrat",sans-serif;font-weight:500;font-size:62px;line-height:150px}
.feature.main .feature-num{width:236px;height:170px;border-radius:0 0 118px 118px;background:var(--blue);font-size:76px;line-height:170px}
.feature-title{margin-top:30px;font-family:"Montserrat",sans-serif;font-weight:700;font-size:20px;color:var(--ink)}
.feature.main .feature-title{margin-top:34px;font-size:25px;color:var(--blue)}
.feature-list{list-style:none;margin-top:14px;font-size:13px;line-height:22px;color:var(--ink)}
.feature.main .feature-list{margin-top:24px;line-height:26px}
.feature .btn{margin-top:20px;background:var(--dark);color:var(--white);font-size:12px;padding:13px 22px}
.feature.main .btn{margin-top:28px;background:var(--blue);font-size:14px;padding:16px 24px}
.feature.certs .btn{margin-top:16px}

.ceo-text{position:absolute;top:1201px;left:99px;width:1002px;text-align:center;font-size:13.5px;line-height:27px;color:var(--text);z-index:2}
.ceo-text p+p{margin-top:22px}

.intro{position:absolute;top:1545px;left:99px;width:640px}
.intro h2{font-family:"Montserrat",sans-serif;font-weight:700;font-size:27px;color:var(--blue)}
.rule{display:block;width:96px;height:3px;background:var(--blue);margin-top:18px}
.intro p{margin-top:30px;font-size:13.5px;line-height:24px;color:var(--ink)}
.intro .btn{margin-top:32px;background:var(--blue);color:var(--white);font-size:13px;padding:14px 20px}
.intro-art{position:absolute;top:1552px;left:790px;width:290px;height:262px;border-radius:40px;background:radial-gradient(circle at 50% 50%,#c9c9c9 0%,#8dd14a 55%,#62b52a 100%)}

.services{position:absolute;top:1907px;left:0;width:1200px;height:793px;background:radial-gradient(ellipse at 50% 40%,#26302f 0%,#141a1b 70%,#0d1112 100%);color:var(--white)}
.services h2{position:absolute;top:88px;width:1200px;text-align:center;font-family:"Montserrat",sans-serif;font-weight:700;font-size:28px}
.services .rule{position:absolute;top:140px;left:562px;width:76px;background:var(--white);margin:0}
.service{position:absolute;top:208px;width:483px;text-align:center}
.service.ewaste{left:99px}.service.pickup{left:616px}
.service-photo{height:234px;border:3px solid var(--white);border-radius:28px}
.service.ewaste .service-photo{background:linear-gradient(160deg,#9a4a43 0%,#5d6b7a 45%,#2f7d3b 100%)}
.service.pickup .service-photo{background:linear-gradient(160deg,#b7b0a4 0%,#8a8378 50%,#3d4a60 100%)}
.service h3{margin-top:40px;font-family:"Montserrat",sans-serif;font-weight:700;font-size:20px}
.service .sub{margin-top:16px;font-size:13px}
.service p.desc{margin:24px auto 0;width:470px;font-size:13.5px;line-height:26px}
.service .btn{margin-top:26px;background:var(--blue);color:var(--white);font-size:12px;padding:13px 20px;border:2px solid var(--white)}

.site-footer{position:absolute;top:2700px;left:0;width:1200px;height:452px}
.footer-brand{position:absolute;top:92px;left:0;width:1200px;display:flex;justify-content:center;align-items:center;gap:14px}
.footer-brand .brand-mark{width:72px;height:72px}
.footer-brand .brand-name{font-size:40px}
.socials{position:absolute;top:222px;left:0;width:1200px;display:flex;justify-content:center;gap:10px}
.socials span{width:40px;height:40px;border:2px solid var(--ink);border-radius:50%}
.footer-nav{position:absolute;top:314px;left:0;width:1200px;display:flex;justify-content:center;gap:40px;font-family:"Montserrat",sans-serif;font-weight:500;font-size:15px;color:var(--ink)}
.footer-line{position:absolute;top:374px;left:99px;width:1002px;height:1px;background:#cfcfcf}
.copyright{position:absolute;top:406px;width:1200px;text-align:center;font-size:15px;color:var(--ink)}
</style>
</head>
<body>

<header class="site-header">
  <a class="brand" href="#"><span class="brand-mark"></span><span class="brand-name">Velno Recycling</span></a>
  <a class="contact-pill mail" href="#">
    <svg width="16" height="12" viewBox="0 0 16 12"><rect x="0.5" y="0.5" width="15" height="11" fill="none" stroke="#fff"/><path d="M1 1l7 6 7-6" fill="none" stroke="#fff"/></svg>
    hello@velnorecycling.com</a>
  <a class="contact-pill phone" href="#">
    <svg width="13" height="13" viewBox="0 0 24 24"><path fill="#fff" d="M6.6 10.8a15 15 0 006.6 6.6l2.2-2.2c.3-.3.7-.4 1-.2 1.1.4 2.3.6 3.6.6.6 0 1 .4 1 1V20c0 .6-.4 1-1 1A17 17 0 013 4c0-.6.4-1 1-1h3.5c.6 0 1 .4 1 1 0 1.3.2 2.5.6 3.6.1.3 0 .7-.2 1z"/></svg>
    (555)014-2270</a>
  <nav class="main-nav"><a href="#">HOME</a><a href="#">ABOUT US</a><a href="#">BOOK ONLINE</a><a href="#">BLOG</a><a href="#">CONTACT US</a></nav>
</header>

<div class="about"></div>

<section class="hero" role="img" aria-label="Photo of a recycling bin full of old electronics in a field with pine trees, under a dark overlay">
  <svg class="hero-arrow prev" width="24" height="46" viewBox="0 0 24 46"><path d="M22 2L2 23l20 21" fill="none" stroke="#fff" stroke-width="2.5"/></svg>
  <svg class="hero-arrow next" width="24" height="46" viewBox="0 0 24 46"><path d="M2 2l20 21L2 44" fill="none" stroke="#fff" stroke-width="2.5"/></svg>
  <div class="hero-body">
    <h1 class="hero-title">VELNO RECYCLING</h1>
    <p class="hero-lead">Want to make a difference to our environment and planet? Velno Recycling is here to help! Velno recycling has been helping keep the environment healthy since 2006.</p>
    <a class="btn" href="#">Read More</a>
  </div>
</section>

<div class="features">
  <article class="feature side logistics">
    <div class="feature-num">1.</div>
    <h3 class="feature-title">LOGISTICS</h3>
    <ul class="feature-list">
      <li>Global Logistics Support</li><li>Global Warehouse Capabilities</li><li>Global Audit Capabilities</li><li>Inventory Management</li><li>Asset Management</li><li>Bill of Lading</li><li>Proof of Delivery</li>
    </ul>
    <a class="btn" href="#">Read More</a>
  </article>
  <article class="feature main">
    <div class="feature-num">2.</div>
    <h3 class="feature-title">RECYCLING</h3>
    <ul class="feature-list">
      <li>Certified Global Recycling Capabilities</li><li>Sort by commodity</li><li>Certificate of Recycling</li><li>Data Destruction</li><li>Verifiable Certified Downstream</li><li>Vendors</li>
    </ul>
    <a class="btn" href="#">Read More</a>
  </article>
  <article class="feature side certs">
    <div class="feature-num">3.</div>
    <h3 class="feature-title">CERTIFICATES</h3>
    <ul class="feature-list">
      <li>R2:2013 Responsible Recycling Certified</li><li>ISO 14001:2015</li><li>OHSAS 18001:2007</li><li>State Board of Environmental Quality</li><li>(SBEQ)</li><li>Regulated Entity # RN550120987</li><li>GDPR Compliant</li>
    </ul>
    <a class="btn" href="#">Read More</a>
  </article>
</div>

<div class="ceo-text">
  <p>As the CEO of Velno Recycling, Dane Whitlow is responsible for running all facets of the business. Dane has a proven executive management track record and over 20 years of experience driving sales growth in the Recycling industry. Prior to founding Velno Recycling in 2006, Dane was the Director of Sales for Norland Device Exchange Inc. and responsible for all global sales and marketing activities.</p>
  <p>At NDE he led the paradigm shifting transformation into an enterprise-focused company while growing sales 50% year over year. Dane was able to accomplish these record setting achievements because of his ability to build relationships, trust, and build rapport with everyone he meets. Today Velno Recycling stands at the fort front of the Electronics Recycling industry by Dane's keen ability to see market solutions.</p>
</div>

<section class="intro">
  <h2>Computer Recycling Made Easy</h2>
  <span class="rule"></span>
  <p>Want to make a difference to our environment and planet? Velno Recycling is here to help! Velno recycling has been helping keep the environment healthy since 2006, we specialize in recycling services that help citizens become experts at reducing waste. We have a passion to keep our world clean and are here to guide you through all the stages of the recycling process.</p>
  <a class="btn" href="#">Read More</a>
</section>
<div class="intro-art" role="img" aria-label="Illustration of old computers and appliances inside a green recycling arrow loop"></div>

<section class="services">
  <h2>RECYCLING SERVICES</h2>
  <span class="rule"></span>
  <article class="service ewaste">
    <div class="service-photo" role="img" aria-label="Photo of people dropping old phones and devices into a green recycling bin"></div>
    <h3>ELECTRONIC RECYCLING</h3>
    <p class="sub">Environmentally Friendly</p>
    <p class="desc">At Velno Recycling, we strive to keep the environment clean through our wide range of services. Our E-Waste Recycling services were designed to simplify the recycling process.</p>
    <a class="btn" href="#">Schedule a Pickup</a>
  </article>
  <article class="service pickup">
    <div class="service-photo" role="img" aria-label="Photo of a worker loading old electronics next to a stone wall and a recycling bin"></div>
    <h3>RECYCLING PICKUP</h3>
    <p class="sub">We Come To You</p>
    <p class="desc">At Velno Recycling, we go out of our way to make sure your recycling process is made easy as possible. Our Recycling Pickup service is designed to simplify all of your recycling needs.</p>
    <a class="btn" href="#">Schedule a Pickup</a>
  </article>
</section>

<footer class="site-footer">
  <div class="footer-brand"><span class="brand-mark"></span><span class="brand-name">Velno Recycling</span></div>
  <div class="socials" aria-label="Social links"><span></span><span></span><span></span><span></span><span></span></div>
  <nav class="footer-nav"><a href="#">HOME</a><span>|</span><a href="#">ABOUT US</a><span>|</span><a href="#">BOOK ONLINE</a><span>|</span><a href="#">BLOG</a><span>|</span><a href="#">CONTACT US</a></nav>
  <div class="footer-line"></div>
  <p class="copyright">Copyrights @ 2018 Velno. All Rights Reserved.</p>
</footer>

</body>
</html>
```